Spring Jubilee Jamboree

This is an annual Church event and We need a colorful and inviting design that includes details for our 2015 Easter Hunt and Community Outreach Event.( the design may include eggs, children of all races, adults, baby chicks, BUT PLEASE NO BUNNIES) Fun for all-children and parents. Free food, haircuts, games, contests, and more. The final design should include contact and sign up information as well as highlight some of the features mentioned above for the event.

Church

```html
<!DOCTYPE html>
<html lang="en">
<head>
<meta charset="utf-8">
<title>Easter Hunt 2015 – Sign Up</title>
<link rel="stylesheet" href="https://fonts.googleapis.com/css2?family=Bebas+Neue&family=Jost:wght@300;400&display=swap">
<style>
  :root {
    --egg: #6decdf;
    --teal: #3a9a8b;
    --white: #fdfefe;
    --rule: #7fe1d8;
    --ink: #2a2a2a;
    --paper: #ffffff;
  }
  html, body {
    margin: 0;
    padding: 0;
    overflow: hidden;
    background: var(--paper);
  }
  .poster {
    position: relative;
    width: 960px;
    height: 1200px;
    overflow: hidden;
    background: var(--paper);
  }
  .egg {
    position: absolute;
    left: 0;
    top: 0;
  }
  .headline {
    position: absolute;
    left: 0;
    width: 960px;
    text-align: center;
    margin: 0;
    white-space: nowrap;
  }
  .intro {
    top: 20px;
    font-family: "Jost", sans-serif;
    font-weight: 400;
    font-size: 45px;
    color: var(--white);
    letter-spacing: 1px;
  }
  .event-name {
    top: 82px;
    font-family: "Bebas Neue", sans-serif;
    font-size: 156px;
    line-height: 1;
    color: var(--teal);
    letter-spacing: 1px;
  }
  .year {
    top: 180px;
    font-family: "Jost", sans-serif;
    font-weight: 300;
    font-size: 282px;
    line-height: 1;
    color: var(--white);
    letter-spacing: 2px;
  }
  .feature {
    font-family: "Bebas Neue", sans-serif;
    font-size: 54px;
    line-height: 1;
    color: var(--teal);
  }
  .feature--audience { top: 420px; }
  .feature--perks { top: 470px; }
  .closing {
    top: 518px;
    font-family: "Jost", sans-serif;
    font-weight: 400;
    font-size: 76px;
    line-height: 1;
    color: var(--white);
    letter-spacing: 14px;
    padding-left: 14px;
    box-sizing: border-box;
  }
  .signup-label {
    position: absolute;
    left: 28px;
    top: 762px;
    margin: 0;
    font-family: "Jost", sans-serif;
    font-weight: 400;
    font-size: 24px;
    letter-spacing: 4px;
    color: var(--ink);
  }
  .signup-lines {
    position: absolute;
    left: 0;
    top: 0;
  }
</style>
</head>
<body>
  <main class="poster">
    <svg class="egg" width="960" height="1200" viewBox="0 0 960 1200" aria-hidden="true">
      <ellipse cx="480" cy="250" rx="383" ry="487" fill="var(--egg)"/>
    </svg>

    <p class="headline intro">get ready…it’s our annual</p>
    <h1 class="headline event-name">EASTER HUNT</h1>
    <p class="headline year">2015</p>
    <p class="headline feature feature--audience">FUN FOR ALL CHILDREN AND PARENTS</p>
    <p class="headline feature feature--perks">FREE FOOD, HAIRCUTS, GAMES, CONTESTS</p>
    <p class="headline closing">AND MORE</p>

    <h2 class="signup-label">SIGN UP</h2>
    <svg class="signup-lines" width="960" height="1200" viewBox="0 0 960 1200" aria-hidden="true">
      <g stroke="var(--rule)" stroke-width="1.6">
        <line x1="23" y1="828" x2="364" y2="828"/>
        <line x1="23" y1="873" x2="364" y2="873"/>
        <line x1="23" y1="917" x2="364" y2="917"/>
        <line x1="23" y1="962" x2="364" y2="962"/>
        <line x1="23" y1="1010" x2="364" y2="1010"/>
        <line x1="20" y1="1055" x2="361" y2="1055"/>
        <line x1="413" y1="828" x2="755" y2="828"/>
        <line x1="413" y1="875" x2="755" y2="875"/>
      </g>
    </svg>
  </main>
</body>
</html>
```